Postcard Design for a Church

The postcard is for a church. This will be going to new movers in the area. I would like it to say "Welcome to the Neighborhood!" somewhere on the postcard. You can say something like like "Transitioning to a new community can be very difficult and sometimes overwhelming. Our goal as a church is to assist and help where needed". You can also say something like "if you're looking for a church home and a place where you'll be embraced, we invite you to worship with us and be our special guest". Our Facebook page is Facebook.com/TheHarborHouseTN. Our Twitter is TheHarborHouse. Our website page is www.TheHarborHouseTN.org. You can list the vision of the church which is "Our vision is to save souls, change lives & impact the community". Please list the address of the church being located in the main auditorium of Marrowdale High School. The time is Sundays at 11am. The address is 7385 Kettering Lane, Brambleton, TN 37412. Our colors are purple and gold. You can also say "We're more than a church, we're a family". I would like it to also say something like "Come and Grow With Us!" My name is Pastor Darnell "WT" Okafor. My wife's name is First Lady Lashonda Okafor. I hope all this makes sense and it's not exactly in order, but I would like to see your designs. Thank you.

```html
<!DOCTYPE html>
<html lang="en">
<head>
<meta charset="utf-8">
<title>The Harbor House – Welcome Postcard</title>
<link rel="stylesheet" href="https://fonts.googleapis.com/css2?family=Alegreya:ital,wght@0,800;1,800&family=Lato:wght@400;700&display=swap">
<style>
  :root {
    --purple: #5a2781;
    --purple-deep: #4a1f6e;
    --purple-text: #6b2d8a;
    --gold: #c8b865;
    --gold-band: #c1b463;
    --ink: #1d1d1d;
    --paper: #ffffff;
    --backdrop: #2b150d;
    --rule: #ececec;
  }
  * { box-sizing: border-box; margin: 0; padding: 0; }
  html, body { width: 1000px; height: 1200px; overflow: hidden; }
  body { background: var(--backdrop); font-family: "Lato", sans-serif; color: var(--ink); position: relative; }

  .card { position: absolute; left: 128px; width: 752px; background: var(--paper); overflow: hidden; }
  .card--front { top: 14px; height: 579px; }
  .card--back { top: 606px; height: 580px; }

  .heading { font-family: "Alegreya", serif; font-weight: 800; color: var(--purple-text); }

  /* Front */
  .brand { position: absolute; left: 34px; top: 22px; width: 184px; text-align: center; }
  .brand__mark { width: 168px; height: 168px; margin: 0 auto; border-radius: 50%; background: var(--purple); border: 6px solid var(--gold); }
  .brand__name { margin-top: 12px; font-family: "Lato", sans-serif; font-weight: 400; font-size: 27px; line-height: 1.05; color: var(--purple-deep); }

  .welcome { position: absolute; left: 262px; top: 30px; font-style: italic; line-height: 1; }
  .welcome__lead { font-size: 54px; }
  .welcome__lead small { font-size: 34px; }
  .welcome__big { display: block; margin: 4px 0 0 60px; font-size: 47px; }

  .dots { position: absolute; height: 6px; background-image: radial-gradient(circle, #7e5a9a 2.2px, transparent 2.6px); background-size: 9px 6px; }
  .card--front .dots { left: 245px; top: 155px; width: 480px; opacity: .8; }

  .intro { position: absolute; left: 262px; top: 180px; width: 456px; font-size: 15.5px; line-height: 20px; text-align: justify; }
  .intro p + p { margin-top: 19px; }

  .vision { position: absolute; left: 261px; top: 330px; width: 470px; font-size: 16px; line-height: 20px; }
  .vision strong { color: var(--purple-text); font-weight: 700; }

  .grow { position: absolute; left: 260px; top: 383px; font-size: 31px; letter-spacing: .3px; }
  .pastors { position: absolute; left: 261px; top: 422px; font-size: 16px; font-weight: 700; }

  .band { position: absolute; left: 0; top: 0; }
  .photo { position: absolute; left: 24px; top: 327px; width: 206px; height: 206px; border-radius: 50%; border: 4px solid #e6dcc4; background: radial-gradient(circle at 50% 40%, #c9b7a8 0%, #7a5e52 45%, #2a2222 100%); }

  .location { position: absolute; left: 260px; top: 511px; color: #fff; font-size: 15.5px; line-height: 22px; }
  .location strong { font-weight: 700; }
  .service { position: absolute; left: 592px; top: 533px; color: #fff; font-size: 15.5px; }

  /* Back */
  .card--back .edge { position: absolute; left: 0; top: 0; }
  .brand--back { left: 111px; top: 28px; width: 200px; }
  .brand--back .brand__mark { width: 120px; height: 120px; border-width: 5px; }
  .brand--back .brand__name { margin-top: 5px; font-size: 16px; white-space: nowrap; }

  .family { position: absolute; left: 86px; top: 192px; width: 258px; text-align: center; font-size: 26px; line-height: 34px; }
  .family span { font-size: 32px; }
  .card--back .dots { left: 77px; top: 313px; width: 280px; opacity: .55; background-image: radial-gradient(circle, #666 1.6px, transparent 2px); background-size: 6px 6px; }

  .social { position: absolute; left: 80px; top: 348px; list-style: none; font-size: 13.5px; }
  .social li { display: flex; align-items: center; gap: 9px; height: 20px; margin-bottom: 14px; }
  .social .dot { width: 19px; height: 19px; border-radius: 50%; background: var(--purple); }

  .website { position: absolute; left: 57px; top: 434px; width: 308px; height: 43px; background: var(--gold-band); display: flex; align-items: center; justify-content: center; font-size: 15px; }

  .stamp { position: absolute; left: 579px; top: 27px; width: 137px; height: 143px; border: 5px solid var(--rule); }
  .address-line { position: absolute; left: 392px; width: 326px; height: 4px; background: var(--rule); }
</style>
</head>
<body>

<section class="card card--front">
  <svg class="band" width="752" height="579" viewBox="0 0 752 579">
    <path d="M0,497 C120,540 250,522 380,490 C520,458 650,462 752,494 L752,579 L0,579 Z" fill="var(--purple)"/>
    <path d="M0,489 C120,532 250,514 380,482 C520,450 650,454 752,486" fill="none" stroke="var(--gold)" stroke-width="6"/>
  </svg>

  <div class="brand">
    <div class="brand__mark"></div>
    <p class="brand__name">The Harbor House</p>
  </div>

  <h1 class="heading welcome">
    <span class="welcome__lead">Welcome <small>to the</small></span>
    <span class="welcome__big">NEIGHBORHOOD!</span>
  </h1>
  <div class="dots"></div>

  <div class="intro">
    <p>Transitioning to a new community can be very difficult and sometimes overwhelming. Our goal as a church is to assist and help where needed.</p>
    <p>If you're looking for a church home and a place where you'll be embraced, we invite you to worship with us and be our special guest.</p>
  </div>

  <p class="vision">OUR VISION IS TO <strong>SAVE SOULS, CHANGE LIVES , IMPACT THE COMMUNITY</strong></p>

  <h2 class="heading grow">COME AND GROW WITH US!</h2>
  <p class="pastors">Pastor Darnell "WT" Okafor &amp; wife Lady Lashonda Okafor</p>

  <div class="photo" role="img" aria-label="Portrait of the pastor and his wife"></div>

  <p class="location"><strong>Marrowdale High School</strong> (main auditorium)<br>7385 Kettering Lane, Brambleton, TN 37412</p>
  <p class="service">Sundays at 11am</p>
</section>

<section class="card card--back">
  <svg class="edge" width="120" height="580" viewBox="0 0 120 580">
    <path d="M0,0 L38,0 C26,150 62,300 56,580 L0,580 Z" fill="var(--purple)"/>
    <path d="M38,0 C26,150 62,300 56,580" fill="none" stroke="var(--gold)" stroke-width="5"/>
  </svg>

  <div class="brand brand--back">
    <div class="brand__mark"></div>
    <p class="brand__name">The Harbor House</p>
  </div>

  <h2 class="heading family">WE'RE MORE THAN<br>A CHURCH,<br>WE'RE <span>A FAMILY</span></h2>
  <div class="dots"></div>

  <ul class="social">
    <li><span class="dot"></span>www.friendpage.com/TheHarborHouseTN</li>
    <li><span class="dot"></span>www.chirpline.com/TheHarborHouse</li>
  </ul>

  <p class="website">www.TheHarborHouseTN.org</p>

  <div class="stamp"></div>
  <div class="address-line" style="top:276px"></div>
  <div class="address-line" style="top:339px"></div>
  <div class="address-line" style="top:401px"></div>
  <div class="address-line" style="top:470px"></div>
</section>

</body>
</html>
```